Corwith Lodge website redesign

After 8 years of our current site, we're ready to upgrade our site design. We'd like to generally make it more modern and clean and build it on a CMS like joomla for easier future maintenance.

Our hotel is a family-owned bed and breakfast that competes against much larger hotel chains in Aspen with fancier rooms and larger pricetags. Our hotel is priced moderately and features tasteful, uniquely-design rooms.

We are looking for a website that will showcase the uniqueness of our rooms, the history of the Lodge, and the friendliness of our staff.

Here are some other hotel sites we like:

http://www.brackenfoldhouse.example/

http://www.tollerpeakhaus.example/

http://www.quarrowstay.example/

*********

Scope of Work - I'm looking for a design AND build. The website should be built out in Joomla as part of the final deliverable.
Updates

Current website: http://www.corwithlodge.example/

Explanation of what design + build means:

I am looking for not only the design of the site, but also for the homepage and one subpage to be built out as well. I do NOT need the entire site built - only for those two pages to be built and I will retrofit the remainder of the pages.

Target Market(s)

travellers evaluating hotels in Aspen, Colorado.

Industry/Entity Type

Hotel

Requirements
Must have
• Must, must, must be based on a joomla template. "Rotating" large main image as central position on homepage is a must (see example websites mentioned above).

Nice to have
• We have an existing online reservation system. It would be nice to evaluate placing a "widget" on the homepage that integrates to the online reservation page. Similar to that feature that the Bracken Fold website has at the foot of the main image on their homepage.

```html
<!DOCTYPE html>
<html lang="en">
<head>
<meta charset="utf-8">
<title>Corwith Lodge – Rooms &amp; Rates</title>
<link href="https://fonts.googleapis.com/css2?family=Questrial&family=Open+Sans:wght@700&display=swap" rel="stylesheet">
<style>
  :root {
    --ink: #111111;
    --paper: #ffffff;
    --accent: #a6c83a;
    --snow: #d7dfea;
    --snow-shade: #9eabc0;
    --forest: #4a5866;
    --forest-deep: #2c3641;
    --lift-orange: #e8762a;
    --wall: #cdb98f;
    --wall-shade: #8a7656;
    --quilt: #5f6796;
    --rule: #000000;
  }
  * { margin: 0; padding: 0; box-sizing: border-box; }
  html, body { width: 1200px; height: 831px; overflow: hidden; background: var(--paper); }
  body { position: relative; font-family: "Questrial", "Century Gothic", sans-serif; color: var(--ink); }

  .brand {
    position: absolute; left: 160px; top: 20px;
    font-family: "Questrial", sans-serif; font-size: 32px; color: var(--ink);
    display: flex; align-items: center; gap: 10px;
  }
  .brand-mark { width: 14px; height: 14px; background: var(--ink); }

  .contact {
    position: absolute; right: 177px; top: 19px; text-align: right;
    font-size: 14px; line-height: 17px;
  }
  .contact .label { color: var(--accent); }

  .main-nav {
    position: absolute; left: 158px; top: 76px; width: 865px;
    display: flex; justify-content: space-between; font-size: 17px;
  }
  .main-nav a { color: var(--ink); text-decoration: none; }

  .hero {
    position: absolute; left: 158px; top: 103px; width: 865px; height: 250px;
    background:
      radial-gradient(ellipse 120px 40px at 180px 215px, rgba(232,118,42,0.85), rgba(232,118,42,0) 70%),
      radial-gradient(ellipse 380px 140px at 20% 10%, rgba(236,240,246,0.95), rgba(236,240,246,0) 70%),
      radial-gradient(ellipse 300px 200px at 75% 60%, rgba(44,54,65,0.75), rgba(44,54,65,0) 75%),
      linear-gradient(165deg, var(--snow) 0%, var(--snow-shade) 40%, var(--forest) 75%, var(--forest-deep) 100%);
  }

  .content {
    position: absolute; left: 160px; top: 375px; width: 861px; height: 384px;
    border-left: 1px dotted var(--ink); border-right: 1px dotted var(--ink);
  }
  .page-title {
    position: absolute; left: 17px; top: 8px;
    font-weight: 400; font-size: 27px; letter-spacing: 0.5px;
  }

  .room-type { position: absolute; top: 87px; }
  .room-type h2 {
    display: flex; align-items: center; gap: 6px;
    font-family: "Open Sans", Verdana, sans-serif; font-weight: 700; font-size: 12px; letter-spacing: 0.6px;
  }
  .room-type .icon { width: 23px; height: 22px; background: var(--ink); border-radius: 3px; display: flex; align-items: center; justify-content: center; }
  .room-photo {
    position: absolute; left: 30px; top: 49px; width: 222px; height: 167px;
    background:
      radial-gradient(ellipse 110px 50px at 50% 80%, rgba(240,236,226,0.9), rgba(240,236,226,0) 75%),
      linear-gradient(180deg, var(--wall) 0%, #bfa67a 55%, var(--wall-shade) 80%, #3d3226 100%);
  }
  .room-photo.deluxe {
    width: 221px;
    background:
      radial-gradient(ellipse 90px 55px at 50% 65%, rgba(95,103,150,0.95), rgba(95,103,150,0) 80%),
      linear-gradient(180deg, #b9a27a 0%, var(--wall) 45%, #8d7b63 75%, #2f2a26 100%);
  }
  .room-note {
    position: absolute; left: 30px; top: 52px; white-space: nowrap;
    font-family: "Open Sans", Verdana, sans-serif; font-weight: 700; font-size: 12px;
  }
  .premium { left: 20px; }
  .deluxe-col { left: 299px; }
  .standard { left: 579px; }

  .sub-nav { position: absolute; top: 356px; left: 0; width: 100%; font-size: 14px; }
  .sub-nav a {
    position: absolute; color: var(--ink); text-decoration: none;
    display: flex; align-items: center; gap: 8px; white-space: nowrap;
  }

  .footer-rule { position: absolute; left: 158px; top: 781px; width: 865px; height: 5px; background: var(--rule); }
  .copyright {
    position: absolute; left: 158px; top: 799px;
    font-family: "Open Sans", Verdana, sans-serif; font-weight: 700; font-size: 11px; letter-spacing: 0.6px;
  }
</style>
</head>
<body>
  <header>
    <div class="brand"><span class="brand-mark"></span>Corwith Lodge</div>
    <div class="contact">
      <div><span class="label">email</span> info@corwithlodge.example</div>
      <div><span class="label">telefone number</span> 0077 481 3092</div>
    </div>
    <nav class="main-nav">
      <a href="#">About the Lodge</a>
      <a href="#">Rooms</a>
      <a href="#">Amenitics</a>
      <a href="#">Aspen information</a>
      <a href="#">Manager´s journal</a>
      <a href="#">Webcams</a>
      <a href="#">Contact us</a>
    </nav>
  </header>

  <div class="hero" role="img" aria-label="Ski chairlifts passing over snowy pine forest"></div>

  <main class="content">
    <h1 class="page-title">ROOMS &amp; RATES</h1>

    <section class="room-type premium">
      <h2><span class="icon"><svg width="14" height="12" viewBox="0 0 14 12"><path d="M2 1l5 5-5 5M7 1l5 5-5 5" fill="none" stroke="#fff" stroke-width="1.8"/></svg></span>PREMIUM ROOMS</h2>
      <div class="room-photo" role="img" aria-label="Premium room with wrought-iron headboard and quilted bed"></div>
    </section>

    <section class="room-type deluxe-col">
      <h2><span class="icon"><svg width="14" height="12" viewBox="0 0 14 12"><path d="M2 1l5 5-5 5M7 1l5 5-5 5" fill="none" stroke="#fff" stroke-width="1.8"/></svg></span>DELUXE ROOMS</h2>
      <div class="room-photo deluxe" role="img" aria-label="Deluxe room with iron canopy bed and patchwork quilt"></div>
    </section>

    <section class="room-type standard">
      <h2><span class="icon"><svg width="14" height="12" viewBox="0 0 14 12"><path d="M2 1l5 5-5 5M7 1l5 5-5 5" fill="none" stroke="#fff" stroke-width="1.8"/></svg></span>STANDARD ROOMS</h2>
      <p class="room-note">Room photos coming soon</p>
    </section>

    <nav class="sub-nav">
      <a href="#" style="left:19px">Overview <svg width="13" height="12" viewBox="0 0 13 12"><path d="M1 1l5 5-5 5M6 1l5 5-5 5" fill="none" stroke="var(--accent)" stroke-width="2"/></svg></a>
      <a href="#" style="left:133px">Premiun rooms <svg width="13" height="12" viewBox="0 0 13 12"><path d="M1 1l5 5-5 5M6 1l5 5-5 5" fill="none" stroke="var(--accent)" stroke-width="2"/></svg></a>
      <a href="#" style="left:289px">Deluxe rooms <svg width="13" height="12" viewBox="0 0 13 12"><path d="M1 1l5 5-5 5M6 1l5 5-5 5" fill="none" stroke="var(--accent)" stroke-width="2"/></svg></a>
      <a href="#" style="left:434px">Standart rooms <svg width="13" height="12" viewBox="0 0 13 12"><path d="M1 1l5 5-5 5M6 1l5 5-5 5" fill="none" stroke="var(--accent)" stroke-width="2"/></svg></a>
      <a href="#" style="left:593px">Hotels fotos gallery <svg width="13" height="12" viewBox="0 0 13 12"><path d="M1 1l5 5-5 5M6 1l5 5-5 5" fill="none" stroke="var(--accent)" stroke-width="2"/></svg></a>
    </nav>
  </main>

  <footer>
    <div class="footer-rule"></div>
    <p class="copyright">copyright: xxx xxxxxx</p>
  </footer>
</body>
</html>
```